Local Service Business Needing Clear Business Card Design

We are needing a business card design to be made for our power washing company. Business cards will be printed on plastic standard sized cards. We're looking for someone who can make a unique and unforgettable design. Double sided and or single sided concepts would be ideal. Of course keeping in mind we are seeking translucent cards but not married to the idea of having them as the main concern is just to have plastic cards to prevent water damage! :D

More info on our company can be found on lakeshorebrightwash.example

Not looking for a list of our services. Simply applying company info and possibly "Commercial Residential Fleet" on them tastefully and appropriate to design is all thats needed.

Phone number for our company is 855-GLO-TEAM or 855-456-8326

Industry/Entity Type

Power Washing

Contact Information for Business Card

Phone, Web URL,

Requirements
Should not have
• Bubbles, water or super distracting graphics. Looking for a simple and clean look. Unfortunately our logo is this way which we may seek to change in the near future.

```html
<!DOCTYPE html>
<html lang="en">
<head>
<meta charset="utf-8">
<title>Lakeshore Brightwash — Business Cards</title>
<link rel="stylesheet" href="https://fonts.googleapis.com/css2?family=Arimo:wght@400&family=Bebas+Neue&display=swap">
<style>
  :root {
    --stage: #1c1c1c;
    --card-front: #00ade6;
    --card-back: #00bdf0;
    --panel-white: #ffffff;
    --art-light: #3cc0f2;
    --art-deep: #0b84e2;
    --ink-light: #ffffff;
    --brand-ink: #0a5fc4;
  }
  * { margin: 0; padding: 0; box-sizing: border-box; }
  html, body {
    width: 1093px;
    height: 1200px;
    overflow: hidden;
    background: var(--stage);
  }
  .stage {
    position: relative;
    width: 1093px;
    height: 1200px;
  }
  .card {
    position: absolute;
    left: 264px;
    width: 580px;
    height: 358px;
    overflow: hidden;
  }
  .card--front { top: 226px; background: var(--card-front); }
  .card--back  { top: 620px; background: var(--card-back); }

  .art-placeholder {
    position: absolute;
    left: 0;
    top: 66px;
    width: 435px;
    height: 292px;
    background: linear-gradient(100deg, var(--art-light) 0%, var(--art-deep) 50%, var(--art-light) 100%);
    opacity: 0.85;
  }
  .logo-panel {
    position: absolute;
    left: 0;
    top: 196px;
    width: 330px;
    height: 162px;
    background: var(--panel-white);
    border-top-right-radius: 60px;
  }

  .contact {
    position: absolute;
    top: 44px;
    right: 25px;
    text-align: right;
    font-family: "Arimo", Arial, sans-serif;
    color: var(--ink-light);
  }
  .contact__line {
    display: flex;
    justify-content: flex-end;
    align-items: center;
    gap: 6px;
    line-height: 22px;
  }
  .contact__phone { font-size: 17px; }
  .contact__web { font-size: 15.5px; }
  .contact__icon { width: 15px; height: 15px; flex: none; }

  .divider {
    position: absolute;
    top: 97px;
    right: 25px;
    width: 60px;
    height: 1px;
    background: var(--ink-light);
    opacity: 0.8;
  }
  .services {
    position: absolute;
    top: 104px;
    right: 25px;
    font-family: "Bebas Neue", Impact, sans-serif;
    font-size: 27px;
    letter-spacing: 0.2px;
    color: var(--ink-light);
    line-height: 1;
  }

  .brand-name {
    position: absolute;
    font-family: "Bebas Neue", Impact, sans-serif;
    line-height: 0.9;
    text-align: center;
  }
  .card--front .brand-name {
    left: 38px;
    top: 240px;
    width: 268px;
    font-size: 48px;
    color: var(--brand-ink);
  }
  .card--back .brand-name {
    left: 0;
    right: 0;
    top: 122px;
    font-size: 66px;
    color: var(--ink-light);
  }
</style>
</head>
<body>
<main class="stage">

  <section class="card card--front" aria-label="Business card front">
    <div class="art-placeholder" role="img" aria-label="Blue water splash illustration sweeping across the card"></div>
    <div class="logo-panel"></div>

    <div class="contact">
      <p class="contact__line contact__phone">
        <span>855-456-8326</span>
        <svg class="contact__icon" viewBox="0 0 24 24" aria-hidden="true">
          <path d="M6.6 10.8a15.1 15.1 0 0 0 6.6 6.6l2.2-2.2a1 1 0 0 1 1-.25 11.4 11.4 0 0 0 3.6.57 1 1 0 0 1 1 1V20a1 1 0 0 1-1 1A17 17 0 0 1 3 4a1 1 0 0 1 1-1h3.5a1 1 0 0 1 1 1c0 1.25.2 2.45.57 3.6a1 1 0 0 1-.25 1Z" fill="none" stroke="currentColor" stroke-width="2"/>
          <path d="M15 3a6 6 0 0 1 6 6M15 7a2 2 0 0 1 2 2" fill="none" stroke="currentColor" stroke-width="2"/>
        </svg>
      </p>
      <p class="contact__line contact__web">
        <span>www.lakeshorebrightwash.example</span>
        <svg class="contact__icon" viewBox="0 0 24 24" aria-hidden="true">
          <g fill="none" stroke="currentColor" stroke-width="1.8">
            <circle cx="12" cy="12" r="10"/>
            <ellipse cx="12" cy="12" rx="4.5" ry="10"/>
            <path d="M2 12h20M4 7h16M4 17h16"/>
          </g>
        </svg>
      </p>
    </div>
    <div class="divider"></div>
    <p class="services">Commercial Residential Fleet</p>

    <p class="brand-name">Lakeshore<br>Brightwash</p>
  </section>

  <section class="card card--back" aria-label="Business card back">
    <p class="brand-name">Lakeshore<br>Brightwash</p>
  </section>

</main>
</body>
</html>
```